Blue Ladle Handcrafted Tomato Ketchup packaging design modern

From the best ingredients there is the best ketchup Blue Handcrafted ketchup are specially formulated for fine dining and drinks, bringing out all the flavors. As the Blue Ladle handcrafted ketchup is otherwise fabulous: Made with wholesome, fully ripe fruits Nothing with half things! All Blue Ladle handcrafted ketchups are pure nature, without any artificial diluents or concentrates. Where tomato is on it, that's all there is to it - guaranteed! the design should be professional and noble despite being trendy. A watcher wants to sell the ketchup as merchandising from our restaurant. but as a single brand positioning. The ketchup is vegan. Dimensions: 6.8 cm Height: 7.8 cm Circumference: 21.6 cm The text down (Text 1-4). The lid of the text the glass packaging is black! Thanks for your efforts. I look forward to your designs.

Target Market(s)

foodies

Font styles to use
Serif
Sans Serif

Colors

Designer to choose colors to be used in the design.

Requirements
Must have
• Title: (Handcrafted Tomato Ketchup) Text One: (Store chilled after opening and consume quickly, pasteurized.) Text Two: (Handcrafted in Switzerland by Brennwald Kulinarik GmbH, Chur www.blueladle-sample.ch) Text Tree: (Tomatoes, White Wine Vinegar, Aceto Balsamico, Brown Cane Sugar, Corn Starch, Spices, Salt) Text For: (200 grams) or (200g) The Logo of Blue Ladle with the Pasta and Wine have to because of the gesety.
Nice to have
• small vegan icon (maybe)
Should not have
• text of the logo (pasta & wine)

```html
<!DOCTYPE html>
<html lang="en">
<head>
<meta charset="utf-8">
<title>Blue Ladle – Handcrafted Tomato Ketchup label</title>
<link rel="stylesheet" href="https://fonts.googleapis.com/css2?family=Josefin+Sans:wght@400;600&family=Lobster+Two:ital,wght@1,400&family=Staatliches&display=swap">
<style>
  :root {
    --backdrop: #ececea;
    --label: #f8f8f6;
    --ink: #1d1d1d;
    --ink-soft: #3a3a3a;
    --tomato-red: #e2475b;
    --tomato-soft: #e96a78;
    --rule: #3a3a3a;
  }
  * { margin: 0; padding: 0; box-sizing: border-box; }
  html, body {
    width: 952px;
    height: 1200px;
    overflow: hidden;
    background: var(--backdrop);
  }
  .label {
    position: absolute;
    left: 36px;
    top: 282px;
    width: 880px;
    height: 636px;
    background: var(--label);
    overflow: hidden;
  }
  .band {
    position: absolute;
    background: var(--tomato-red);
  }
  .band--top { left: 568px; top: 68px; width: 312px; height: 48px; }
  .band--bottom { left: 0; top: 560px; width: 530px; height: 40px; }
  .net-weight {
    position: absolute;
    right: 22px;
    top: 0;
    line-height: 48px;
    font-family: "Josefin Sans", sans-serif;
    font-weight: 600;
    font-size: 20px;
    letter-spacing: 0.12em;
    color: var(--label);
  }
  .rule {
    position: absolute;
    height: 3px;
    background: var(--rule);
  }
  .rule--top { left: 575px; top: 150px; width: 215px; }
  .rule--title { left: 560px; top: 212px; width: 200px; }
  .brand {
    position: absolute;
    left: 64px;
    top: 92px;
    font-family: "Josefin Sans", sans-serif;
    font-weight: 400;
    font-size: 46px;
    letter-spacing: 0.16em;
    color: var(--ink);
    text-transform: uppercase;
  }
  .tagline {
    position: absolute;
    left: 56px;
    top: 158px;
    font-family: "Lobster Two", cursive;
    font-style: italic;
    font-size: 78px;
    color: var(--tomato-red);
    line-height: 1;
  }
  .product-name {
    position: absolute;
    left: 54px;
    top: 238px;
    font-family: "Staatliches", sans-serif;
    font-weight: 400;
    font-size: 134px;
    line-height: 1;
    color: var(--ink);
    letter-spacing: 0.01em;
    white-space: nowrap;
  }
  .product-info {
    position: absolute;
    left: 64px;
    top: 414px;
    width: 450px;
    font-family: "Josefin Sans", sans-serif;
    font-size: 14px;
    line-height: 1.45;
    color: var(--ink-soft);
  }
  .product-info p + p { margin-top: 6px; }
  .product-info strong { font-weight: 600; color: var(--ink); }
  .tomato-art {
    position: absolute;
    left: 540px;
    top: 390px;
    width: 290px;
    height: 200px;
    border-radius: 48% 52% 46% 54%;
    background: radial-gradient(ellipse at 40% 45%, var(--tomato-soft), var(--tomato-red) 70%);
  }
</style>
</head>
<body>
  <main class="label">
    <div class="band band--top"><span class="net-weight">200 g</span></div>
    <div class="rule rule--top"></div>

    <p class="brand">Blue Ladle</p>
    <p class="tagline">Handcrafted</p>
    <div class="rule rule--title"></div>
    <h1 class="product-name">Tomato Ketchup</h1>

    <section class="product-info">
      <p><strong>Ingredients:</strong> Tomatoes, White Wine Vinegar, Aceto Balsamico, Brown Cane Sugar, Corn Starch, Spices, Salt</p>
      <p>Store chilled after opening and consume quickly, pasteurized.</p>
      <p>Handcrafted in Switzerland by Brennwald Kulinarik GmbH, Chur www.blueladle-sample.ch</p>
    </section>

    <div class="tomato-art" role="img" aria-label="Sketched illustration of two ripe red tomatoes with green stems"></div>

    <div class="band band--bottom"></div>
  </main>
</body>
</html>
```